Summit Glossfloor & Honing
I'm looking for a business card and logo design for my
new Polished Concrete & Grinding business,
If you were to look up Summit in the dictionary it would
say, first in importance, order, or position; leading.
Polished Concrete floors are a niche market, that are being used currently in Shopping centres, office spaces and by most high end architects, builders and designers.
i need my business card & logo to stand out from my
competitors, i need my design + logo to reflect this it
needs to be simple, professional, eye catching, easy
to read and scream quality. The logo will need to be
suitable for a whole range of applications including,
uniforms, letter heads, stickers, and eventually
incorporating in vehicle vinyl wrapping.
Target Market(s)
Builders, architects, Interior designers & home owners
Contact Information for Business Card
Front side:
- Summit Glossfloor & Honing.
- Logo
Rear side:
- Liam Varga
- 0491735082
- info@summitgfh.com.au
- commercial - domestic - industrial
- (later down the line website & space for
social media links
www.summitglossfloor.com.au)
Colors
Designer to choose colors to be used in the design.
Look and feel

```html
<!DOCTYPE html>
<html lang="en">
<head>
<meta charset="utf-8">
<title>Summit Glossfloor &amp; Honing – Business Card</title>
<link href="https://fonts.googleapis.com/css2?family=Exo+2:wght@600&family=Arimo:wght@400&display=swap" rel="stylesheet">
<style>
  :root {
    --page-bg: #e6e2dc;
    --card-top: #f4f6f7;
    --card-bottom: #e3e7ea;
    --brand-blue: #1d7fbf;
    --brand-blue-light: #3d9fd6;
    --swoosh-grey: #8e9396;
    --text-dark: #3a3f44;
    --text-grey: #7c8288;
    --white: #ffffff;
  }
  html, body {
    margin: 0;
    width: 1200px;
    height: 970px;
    overflow: hidden;
    background: var(--page-bg);
  }
  .business-card {
    position: absolute;
    left: 80px;
    top: 188px;
    width: 1040px;
    height: 594px;
    border-radius: 32px;
    overflow: hidden;
    background: linear-gradient(180deg, var(--card-top), var(--card-bottom));
    box-shadow: 0 14px 40px rgba(0,0,0,0.18);
    font-family: "Arimo", Arial, sans-serif;
  }
  .card-shapes { position: absolute; inset: 0; }
  .social-links {
    position: absolute;
    top: 78px;
    right: 48px;
    display: flex;
    gap: 18px;
  }
  .social-link {
    display: flex;
    align-items: center;
    gap: 6px;
    color: var(--white);
    font-size: 15px;
  }
  .social-link::before {
    content: "";
    width: 12px;
    height: 12px;
    border: 2px solid var(--white);
    border-radius: 50%;
  }
  .wordmark {
    position: absolute;
    left: 55px;
    top: 238px;
    display: flex;
    align-items: center;
    gap: 18px;
  }
  .wordmark-square {
    width: 44px;
    height: 44px;
    background: var(--brand-blue);
  }
  .wordmark-name {
    font-family: "Exo 2", sans-serif;
    font-weight: 600;
    font-size: 42px;
    line-height: 1.05;
    color: var(--brand-blue);
  }
  .person-name {
    position: absolute;
    left: 55px;
    top: 402px;
    margin: 0;
    font-family: "Exo 2", sans-serif;
    font-weight: 600;
    font-size: 32px;
    color: var(--brand-blue);
  }
  .divider {
    position: absolute;
    left: 55px;
    top: 450px;
    width: 928px;
    height: 2px;
    background: var(--brand-blue);
  }
  .contact-list, .service-list {
    position: absolute;
    list-style: none;
    margin: 0;
    padding: 0;
    font-size: 24px;
    line-height: 31px;
    color: var(--text-dark);
  }
  .contact-list { left: 52px; top: 464px; }
  .contact-item { display: flex; align-items: center; gap: 12px; }
  .contact-icon { width: 26px; height: 26px; flex: none; }
  .service-list { right: 52px; top: 468px; text-align: right; }
  .service-item::after {
    content: "";
    display: inline-block;
    width: 9px;
    height: 9px;
    margin-left: 16px;
    border-radius: 50%;
    background: var(--brand-blue);
    vertical-align: middle;
  }
</style>
</head>
<body>
  <main class="business-card">
    <svg class="card-shapes" viewBox="0 0 1040 594" width="1040" height="594" aria-hidden="true">
      <defs>
        <linearGradient id="band-gradient" x1="0" y1="0" x2="1" y2="1">
          <stop offset="0" stop-color="var(--brand-blue-light)"/>
          <stop offset="1" stop-color="var(--brand-blue)"/>
        </linearGradient>
      </defs>
      <path class="top-band" fill="url(#band-gradient)"
            d="M0 0 H1040 V375 C975 215 820 78 470 62 C300 56 130 68 0 80 Z"/>
      <path class="swoosh" fill="var(--swoosh-grey)" opacity="0.8"
            d="M30 86 C180 70 330 62 470 66 C810 80 960 215 1040 380 V440 C950 260 800 100 470 74 C320 68 180 78 30 86 Z"/>
    </svg>

    <nav class="social-links" aria-label="Social media">
      <span class="social-link">Facetly</span>
      <span class="social-link">Chirpa</span>
      <span class="social-link">Snapgrid</span>
      <span class="social-link">Orbitly</span>
    </nav>

    <div class="wordmark">
      <span class="wordmark-square"></span>
      <span class="wordmark-name">Summit Glossfloor<br>&amp; Honing</span>
    </div>

    <h1 class="person-name">Liam Varga</h1>
    <div class="divider"></div>

    <ul class="contact-list">
      <li class="contact-item">
        <svg class="contact-icon" viewBox="0 0 26 26" aria-hidden="true">
          <circle cx="13" cy="13" r="11.5" fill="none" stroke="var(--brand-blue)" stroke-width="2"/>
          <rect x="9" y="6" width="8" height="14" rx="1.5" fill="none" stroke="var(--brand-blue)" stroke-width="1.8"/>
        </svg>0491735082</li>
      <li class="contact-item">
        <svg class="contact-icon" viewBox="0 0 26 26" aria-hidden="true">
          <circle cx="13" cy="13" r="11.5" fill="none" stroke="var(--brand-blue)" stroke-width="2"/>
          <rect x="7" y="8.5" width="12" height="9" fill="var(--brand-blue)"/>
          <path d="M7 8.5 L13 14 L19 8.5" fill="none" stroke="var(--white)" stroke-width="1.4"/>
        </svg>info@summitgfh.com.au</li>
      <li class="contact-item">
        <svg class="contact-icon" viewBox="0 0 26 26" aria-hidden="true">
          <circle cx="13" cy="13" r="11.5" fill="none" stroke="var(--brand-blue)" stroke-width="2"/>
          <circle cx="13" cy="13" r="7" fill="var(--brand-blue)"/>
          <path d="M6 13 H20 M13 6 V20 M8 9 H18 M8 17 H18" stroke="var(--white)" stroke-width="1"/>
        </svg>www.summitglossfloor.com.au</li>
    </ul>

    <ul class="service-list">
      <li class="service-item">Commercial</li>
      <li class="service-item">Domestic</li>
      <li class="service-item">Industrial</li>
    </ul>
  </main>
</body>
</html>
```